Letterhead and Stationary for Construction Company

Brisk Current needs modern Letterhead, Envelopes and Notepad designs.

Industry/Entity Type

Construction

Colors
f78f20
34a7d8
ffffff

Requirements
Must have
• Modern looking design.

```html
<!DOCTYPE html>
<html lang="en">
<head>
<meta charset="UTF-8">
<title>Brisk Current Stationery</title>
<link rel="stylesheet" href="https://fonts.googleapis.com/css2?family=Open+Sans:wght@400;600;700&family=Merriweather:wght@300;400&display=swap">
<style>
  :root{
    --orange:#f78f20;
    --blue:#34a7d8;
    --white:#ffffff;
    --paper:#fbfbfb;
    --ink:#4a4a4a;
    --muted:#8a8a8a;
    --stock:#2a2a2c;
    --stock-edge:#1d1d1f;
    --gold:#c9964a;
    --backdrop:#e6e6e8;
  }
  *{margin:0;padding:0;box-sizing:border-box}
  html,body{width:1200px;height:900px;overflow:hidden;background:var(--backdrop)}
  .canvas{position:relative;width:1200px;height:900px}

  /* Letterhead */
  .letterhead{position:absolute;left:70px;top:140px;width:440px;height:622px;background:var(--paper);
    box-shadow:0 6px 20px rgba(0,0,0,.12);font-family:'Merriweather',serif;color:var(--ink);overflow:hidden}
  .letterhead__band--orange{position:absolute;left:16px;top:0;width:12px;height:62px;background:var(--orange)}
  .letterhead__band--blue{position:absolute;left:16px;top:96px;width:12px;bottom:0;background:var(--blue)}
  .brand{position:absolute;display:flex;align-items:center;gap:8px;font-family:'Open Sans',sans-serif;font-weight:700}
  .brand__dot{border-radius:50%;flex:none}
  .letterhead .brand{left:12px;top:66px}
  .letterhead .brand__dot{width:22px;height:22px;background:var(--blue)}
  .letterhead .brand__name{font-size:17px;color:var(--orange);letter-spacing:.2px}
  .letterhead__top-rule{position:absolute;left:170px;right:24px;top:78px;height:2px;background:var(--orange)}
  .recipient{position:absolute;left:52px;top:120px;font-size:9px;color:var(--blue);font-family:'Open Sans',sans-serif;font-weight:600}
  .date{position:absolute;right:30px;top:120px;font-size:8px;color:var(--muted)}
  .body{position:absolute;left:52px;right:30px;top:150px;font-size:8.5px;line-height:1.75;font-weight:300}
  .body p{margin-bottom:12px}
  .signoff{position:absolute;right:36px;top:430px;text-align:right}
  .signoff__name{font-family:'Open Sans',sans-serif;font-weight:700;font-size:9px}
  .signoff__title{font-size:7px;color:var(--muted)}
  .signoff__signature{width:70px;height:22px;margin:6px 0 0 auto;background:linear-gradient(90deg,rgba(60,60,60,.08),rgba(60,60,60,.25),rgba(60,60,60,.08));border-radius:3px}
  .contacts{position:absolute;left:40px;bottom:34px;list-style:none;font-size:7.5px;color:var(--muted);font-family:'Open Sans',sans-serif}
  .contacts li{display:flex;align-items:center;gap:8px;margin-top:7px}
  .contacts svg{width:16px;height:16px;flex:none}
  .corner-dots{position:absolute;right:-8px;bottom:54px;width:40px;height:60px}

  /* Envelope */
  .envelope{position:absolute;left:570px;top:130px;width:580px;height:300px;background:var(--stock);
    box-shadow:0 8px 22px rgba(0,0,0,.25)}
  .envelope__flap{position:absolute;inset:0}
  .envelope__seal{position:absolute;left:262px;top:96px;width:54px;height:54px;border-radius:50%;
    background:radial-gradient(circle at 40% 40%,#e4c27a,#a67a32)}
  .envelope .brand{left:50%;top:196px;transform:translateX(-50%)}
  .envelope .brand__dot{width:24px;height:24px;background:#d8d8d8}
  .envelope .brand__name{font-size:24px;color:#d8d8d8;font-weight:600}

  /* Notepad */
  .notepad{position:absolute;left:600px;top:480px;width:520px;height:330px;background:var(--stock);
    box-shadow:0 8px 22px rgba(0,0,0,.25)}
  .notepad__spiral{position:absolute;left:18px;right:18px;top:-8px;height:20px}
  .notepad .brand{left:50%;top:148px;transform:translateX(-50%)}
  .notepad .brand__dot{width:24px;height:24px;background:var(--gold)}
  .notepad .brand__name{font-size:24px;color:var(--gold);font-weight:600}
</style>
</head>
<body>
<main class="canvas">

  <section class="letterhead" aria-label="Letterhead">
    <div class="letterhead__band--orange"></div>
    <div class="letterhead__band--blue"></div>
    <div class="brand"><span class="brand__dot"></span><span class="brand__name">Brisk Current</span></div>
    <div class="letterhead__top-rule"></div>

    <p class="recipient">To: Jane Reader</p>
    <p class="date">July 14, 2024</p>

    <div class="body">
      <p>Thank you for choosing our team for your upcoming build. We have reviewed the site plans and prepared a full schedule covering groundwork, framing, roofing and final finishes. Our crews will start once permits are approved, and a project lead will keep you informed at every stage of the work.</p>
      <p>Enclosed you will find the cost summary and material list. Please review them and contact our office with any questions before signing.</p>
    </div>

    <div class="signoff">
      <p class="signoff__name">Sam Porter</p>
      <p class="signoff__title">Site Manager</p>
      <div class="signoff__signature" role="img" aria-label="Handwritten signature"></div>
    </div>

    <ul class="contacts">
      <li><svg viewBox="0 0 16 16"><circle cx="8" cy="8" r="8" fill="#f78f20"/><path d="M5.5 4.5l1.5 1.6-.8 1.1a5 5 0 0 0 2.6 2.6l1.1-.8 1.6 1.5-.9 1.2c-3 0-6.3-3.3-6.3-6.3z" fill="#fff"/></svg>+00 123 456 7890</li>
      <li><svg viewBox="0 0 16 16"><circle cx="8" cy="8" r="8" fill="#f78f20"/><path d="M8 3.5a3 3 0 0 1 3 3c0 2.2-3 5.8-3 5.8s-3-3.6-3-5.8a3 3 0 0 1 3-3z" fill="#fff"/><circle cx="8" cy="6.5" r="1.1" fill="#f78f20"/></svg>12 Harbour Lane, Westford</li>
      <li><svg viewBox="0 0 16 16"><circle cx="8" cy="8" r="8" fill="#f78f20"/><circle cx="8" cy="8" r="4" fill="none" stroke="#fff" stroke-width="1"/><path d="M4 8h8M8 4c-1.8 2.4-1.8 5.6 0 8M8 4c1.8 2.4 1.8 5.6 0 8" fill="none" stroke="#fff" stroke-width=".8"/></svg>www.briskcurrent.example</li>
    </ul>

    <svg class="corner-dots" viewBox="0 0 40 60">
      <circle cx="28" cy="10" r="8" fill="#f78f20"/>
      <circle cx="20" cy="30" r="8" fill="#f78f20"/>
      <circle cx="30" cy="50" r="8" fill="#f78f20"/>
    </svg>
  </section>

  <section class="envelope" aria-label="Envelope">
    <svg class="envelope__flap" viewBox="0 0 580 300" preserveAspectRatio="none">
      <polyline points="0,0 290,130 580,0" fill="none" stroke="#3a3a3d" stroke-width="2"/>
    </svg>
    <div class="envelope__seal" role="img" aria-label="Gold wax seal"></div>
    <div class="brand"><span class="brand__dot"></span><span class="brand__name">Brisk Current</span></div>
  </section>

  <section class="notepad" aria-label="Notepad cover">
    <svg class="notepad__spiral" viewBox="0 0 484 20" preserveAspectRatio="none">
      <g fill="none" stroke="#9a9a9a" stroke-width="2">
        <ellipse cx="12" cy="10" rx="4" ry="8"/><ellipse cx="32" cy="10" rx="4" ry="8"/><ellipse cx="52" cy="10" rx="4" ry="8"/><ellipse cx="72" cy="10" rx="4" ry="8"/><ellipse cx="92" cy="10" rx="4" ry="8"/><ellipse cx="112" cy="10" rx="4" ry="8"/><ellipse cx="132" cy="10" rx="4" ry="8"/><ellipse cx="152" cy="10" rx="4" ry="8"/><ellipse cx="172" cy="10" rx="4" ry="8"/><ellipse cx="192" cy="10" rx="4" ry="8"/><ellipse cx="212" cy="10" rx="4" ry="8"/><ellipse cx="232" cy="10" rx="4" ry="8"/><ellipse cx="252" cy="10" rx="4" ry="8"/><ellipse cx="272" cy="10" rx="4" ry="8"/><ellipse cx="292" cy="10" rx="4" ry="8"/><ellipse cx="312" cy="10" rx="4" ry="8"/><ellipse cx="332" cy="10" rx="4" ry="8"/><ellipse cx="352" cy="10" rx="4" ry="8"/><ellipse cx="372" cy="10" rx="4" ry="8"/><ellipse cx="392" cy="10" rx="4" ry="8"/><ellipse cx="412" cy="10" rx="4" ry="8"/><ellipse cx="432" cy="10" rx="4" ry="8"/><ellipse cx="452" cy="10" rx="4" ry="8"/><ellipse cx="472" cy="10" rx="4" ry="8"/>
      </g>
    </svg>
    <div class="brand"><span class="brand__dot"></span><span class="brand__name">Brisk Current</span></div>
  </section>

</main>
</body>
</html>
```